Marrow Business Cards

Front of business card will have logo, name, address, & telephone number. Back of card will have a list of services provided - Roads, Substation Pads, Temporary Pads, Site Pads, Land Leveling, Powerline Row Cleaning, Land Clearing, Gates, Fencing, Construction Entrances, Excavation, Trenching, Underground Utilities, Directional Boring, Pile Driving. We are a construction company that uses heavy equipment like bulldozers, motor graders/blades, dump trucks, backhoes, hydro axes, & skid loaders. We build roads, pads, & install electric utility lines & waterlines underground. This logo is new. The word "Construction" can be smaller as uploaded 2 example edited logos. We will be using this card design for many employees.
Target Market(s)
Industrial Electric Powerline, Wind Turbine, Solar Panel, & Water Utility companies.
Contact Information for Business Card
Name/Position - Dorian Quale - Owner
Address: 4837 FM 582
Harlow, NM 87612
Phone number - (505) 418-2906

```html
<!DOCTYPE html>
<html lang="en">
<head>
<meta charset="UTF-8">
<title>Marrow Construction – Business Cards</title>
<link rel="stylesheet" href="https://fonts.googleapis.com/css2?family=Archivo+Black&family=Exo+2:wght@500&family=Marcellus&family=Montserrat:wght@500;600&display=swap">
<style>
  :root {
    --stage: #2b2b2d;
    --maroon: #5a1a28;
    --maroon-dark: #3f0f1b;
    --paper: #ffffff;
    --ink: #151515;
    --muted: #444444;
    --on-maroon: #ffffff;
    --rule-light: rgba(255,255,255,0.85);
  }
  * { box-sizing: border-box; margin: 0; padding: 0; }
  html, body { width: 1200px; height: 1200px; overflow: hidden; }
  body {
    background: var(--stage);
    display: flex;
    flex-direction: column;
    align-items: center;
    justify-content: center;
    gap: 44px;
    font-family: "Montserrat", sans-serif;
  }
  .card {
    width: 900px;
    height: 514px;
    display: grid;
    grid-template-columns: 1fr 2px 1fr;
    align-items: center;
    box-shadow: 0 10px 30px rgba(0,0,0,0.45);
  }
  .card--back {
    background: linear-gradient(135deg, var(--maroon) 0%, var(--maroon-dark) 100%);
    color: var(--on-maroon);
  }
  .card--front { background: var(--paper); color: var(--ink); }

  .brand {
    display: flex;
    align-items: center;
    justify-content: center;
    gap: 14px;
    font-family: "Marcellus", serif;
    font-size: 32px;
    letter-spacing: 0.04em;
    line-height: 1.15;
  }
  .brand__dot { width: 18px; height: 18px; border-radius: 50%; flex: none; }
  .card--back .brand { color: var(--on-maroon); }
  .card--back .brand__dot { background: var(--on-maroon); }
  .card--front .brand { color: var(--maroon); }
  .card--front .brand__dot { background: var(--maroon); }

  .divider { width: 2px; }
  .card--back .divider { background: var(--rule-light); height: 380px; }
  .card--front .divider { background: var(--maroon); height: 190px; }

  .services {
    list-style: none;
    padding-left: 36px;
    font-family: "Exo 2", sans-serif;
    font-weight: 500;
    font-size: 19px;
    letter-spacing: 0.04em;
    line-height: 27px;
  }
  .services li { display: flex; align-items: center; gap: 12px; }
  .services svg { width: 20px; height: 10px; flex: none; fill: var(--on-maroon); }

  .contact { padding-left: 40px; }
  .contact__name {
    font-family: "Archivo Black", sans-serif;
    font-size: 28px;
    letter-spacing: 0.04em;
    text-transform: uppercase;
    line-height: 1;
  }
  .contact__role {
    font-size: 17px;
    letter-spacing: 0.08em;
    color: var(--muted);
    margin-top: 6px;
    text-transform: uppercase;
  }
  .contact__lines { list-style: none; margin-top: 28px; font-size: 21px; font-weight: 500; line-height: 36px; }
  .contact__lines li { display: flex; align-items: center; gap: 12px; white-space: nowrap; }
  .contact__lines svg { width: 20px; height: 20px; fill: var(--ink); flex: none; }
</style>
</head>
<body>

<section class="card card--back" aria-label="Card back – services">
  <div class="brand"><span class="brand__dot"></span><span>MARROW<br>CONSTRUCTION</span></div>
  <div class="divider"></div>
  <ul class="services">
    <li><svg viewBox="0 0 20 10"><path d="M0 3h12V0l8 5-8 5V7H0z"/></svg>Roads</li>
    <li><svg viewBox="0 0 20 10"><path d="M0 3h12V0l8 5-8 5V7H0z"/></svg>Substation Pads</li>
    <li><svg viewBox="0 0 20 10"><path d="M0 3h12V0l8 5-8 5V7H0z"/></svg>Temporary Pads</li>
    <li><svg viewBox="0 0 20 10"><path d="M0 3h12V0l8 5-8 5V7H0z"/></svg>Site Pads</li>
    <li><svg viewBox="0 0 20 10"><path d="M0 3h12V0l8 5-8 5V7H0z"/></svg>Land Leveling</li>
    <li><svg viewBox="0 0 20 10"><path d="M0 3h12V0l8 5-8 5V7H0z"/></svg>Powerline Row Cleaning</li>
    <li><svg viewBox="0 0 20 10"><path d="M0 3h12V0l8 5-8 5V7H0z"/></svg>Land Clearing</li>
    <li><svg viewBox="0 0 20 10"><path d="M0 3h12V0l8 5-8 5V7H0z"/></svg>Gates</li>
    <li><svg viewBox="0 0 20 10"><path d="M0 3h12V0l8 5-8 5V7H0z"/></svg>Fencing</li>
    <li><svg viewBox="0 0 20 10"><path d="M0 3h12V0l8 5-8 5V7H0z"/></svg>Construction Entrances</li>
    <li><svg viewBox="0 0 20 10"><path d="M0 3h12V0l8 5-8 5V7H0z"/></svg>Excavation</li>
    <li><svg viewBox="0 0 20 10"><path d="M0 3h12V0l8 5-8 5V7H0z"/></svg>Trenching</li>
    <li><svg viewBox="0 0 20 10"><path d="M0 3h12V0l8 5-8 5V7H0z"/></svg>Underground Utilities</li>
    <li><svg viewBox="0 0 20 10"><path d="M0 3h12V0l8 5-8 5V7H0z"/></svg>Directional Boring</li>
    <li><svg viewBox="0 0 20 10"><path d="M0 3h12V0l8 5-8 5V7H0z"/></svg>Pile Driving.</li>
  </ul>
</section>

<section class="card card--front" aria-label="Card front – contact">
  <div class="brand"><span class="brand__dot"></span><span>MARROW<br>CONSTRUCTION</span></div>
  <div class="divider"></div>
  <div class="contact">
    <p class="contact__name">Dorian Quale</p>
    <p class="contact__role">Owner</p>
    <ul class="contact__lines">
      <li><svg viewBox="0 0 24 24"><path d="M12 2a7 7 0 0 0-7 7c0 5.2 7 13 7 13s7-7.8 7-13a7 7 0 0 0-7-7zm0 9.5A2.5 2.5 0 1 1 12 6.5a2.5 2.5 0 0 1 0 5z"/></svg>4837 FM 582, Harlow, NM 87612</li>
      <li><svg viewBox="0 0 24 24"><path d="M6.6 10.8a15.1 15.1 0 0 0 6.6 6.6l2.2-2.2c.3-.3.7-.4 1-.2 1.1.4 2.3.6 3.6.6.6 0 1 .4 1 1V20c0 .6-.4 1-1 1A17 17 0 0 1 3 4c0-.6.4-1 1-1h3.5c.6 0 1 .4 1 1 0 1.3.2 2.5.6 3.6.1.3 0 .7-.2 1z"/></svg>(505) 418-2906</li>
    </ul>
  </div>
</section>

</body>
</html>
```